Junk Removal company with existing WordPress website needs new mobile enhanced website

I am looking to have someone take my existing website and either update it with a new design and menu which is more mobile enhanced (70% of my traffic is from mobile devices and most people stay on the home page to find what they need) or create a new website from scratch to achieve my design goals. My name goal is the have to home page be quick and easy to find what the customer is looking for.
Our current website is: BrightmoorJunkCarters.com and Google my business page https://g.page/brightmoorjunkcarters
I have attached an example the design idea I came up with for the home page based on what I would like it to look like as well as some logo files and pictures.

```html
<!DOCTYPE html>
<html lang="en">
<head>
<meta charset="utf-8">
<title>Brightmoor Junk Carters – Junk Removal & Property Cleanouts</title>
<link href="https://fonts.googleapis.com/css2?family=Saira+Condensed:wght@600;700&family=Poppins:wght@300;400;500;600&display=swap" rel="stylesheet">
<style>
:root{
  --orange:#f7901e;
  --orange-deep:#ef6a12;
  --orange-soft:#fde8cf;
  --cream:#fff8e8;
  --ink:#111111;
  --text:#333333;
  --muted:#777777;
  --band:#0c0c0c;
  --line:#e6e6e6;
}
*{margin:0;padding:0;box-sizing:border-box}
html,body{width:1200px;height:4468px;overflow:hidden}
body{position:relative;background:#fff;font-family:"Poppins",sans-serif;color:var(--text)}
.abs{position:absolute}
.display{font-family:"Saira Condensed",sans-serif;font-weight:700;font-variant:small-caps;letter-spacing:.5px;color:var(--ink)}
.accent{color:var(--orange-deep)}
.btn{display:inline-block;background:linear-gradient(90deg,var(--orange),var(--orange-deep));color:#fff;border-radius:24px;font-family:"Saira Condensed",sans-serif;font-weight:700;font-variant:small-caps;font-size:19px;text-align:center}
.photo{position:absolute}

/* header */
.site-header{top:0;left:0;width:1200px;height:70px;background:#fff;box-shadow:0 2px 6px rgba(0,0,0,.08);z-index:5}
.brand{left:58px;top:12px;display:flex;align-items:center;gap:10px}
.brand-dot{width:44px;height:44px;border-radius:50%;background:var(--orange)}
.brand-name{font-family:"Saira Condensed",sans-serif;font-weight:700;font-size:22px;line-height:22px;color:var(--ink);width:150px}
.nav{left:492px;top:20px;display:flex;align-items:center;gap:20px;font-size:11px;font-weight:500;color:var(--ink)}
.nav .active{background:var(--orange);color:#fff;padding:8px 16px;border-radius:18px}
.nav-phone{left:986px;top:16px;width:180px;height:38px;border-radius:20px;background:var(--orange);display:flex;align-items:center;font-family:"Saira Condensed",sans-serif;font-weight:700;font-size:17px;color:var(--ink)}
.nav-phone i{width:38px;height:38px;border-radius:50%;background:var(--ink);margin-right:10px;display:flex;align-items:center;justify-content:center}

/* hero */
.hero-tag{left:90px;top:272px;font-family:"Saira Condensed",sans-serif;font-weight:700;font-variant:small-caps;font-size:22px;color:var(--orange-deep)}
.hero-title{left:88px;top:305px;font-size:40px;line-height:46px;width:480px;text-transform:uppercase;font-variant:normal}
.hero-btns{left:90px;top:464px;display:flex;gap:12px}
.hero-btns .btn{width:125px;height:42px;line-height:42px}
.scroll{left:20px;top:505px;transform:rotate(-90deg);transform-origin:left top;font-size:11px;color:var(--text)}
.scroll-line{left:32px;top:520px;width:1px;height:105px;background:#999}

.band{top:728px;left:0;width:1200px;height:77px;background:var(--band);display:flex;align-items:center;justify-content:center;gap:14px}
.band p{font-family:"Saira Condensed",sans-serif;font-weight:700;font-variant:small-caps;font-size:20px;color:#fff}
.band .btn{width:124px;height:40px;line-height:40px}

/* about */
.about-bg{top:805px;left:0;width:1200px;height:357px;background:linear-gradient(90deg,#fff 40%,#f4f4f4)}
.about-eyebrow{left:592px;top:882px;font-size:13px;color:var(--muted)}
.about-title{left:590px;top:900px;font-size:36px}
.about-copy{left:592px;top:960px;width:510px;font-size:11.5px;line-height:20px;color:var(--muted)}
.about-call{left:592px;top:1060px;font-size:21px;font-family:"Saira Condensed",sans-serif;font-weight:700;font-variant:small-caps;color:var(--orange-deep)}

/* services */
.eyebrow{width:1200px;left:0;text-align:center;font-size:13px;color:var(--muted)}
.section-title{width:1200px;left:0;text-align:center;font-size:38px}
.card{top:1333px;width:330px;height:522px;background:var(--cream);padding:8px}
.card .photo{position:relative;width:314px;height:192px}
.card h3{font-size:21px;margin:22px 0 12px 18px}
.card ul{list-style:none;margin-left:20px}
.card li{font-size:11.5px;line-height:24.5px;color:var(--text);display:flex;align-items:center;gap:12px}
.card li::before{content:"";width:6px;height:6px;border:2px solid var(--orange-deep);transform:rotate(45deg)}
.pitch{top:1912px;left:0;width:1200px;text-align:center;font-size:25px;line-height:36px}
.call-box{left:410px;top:2010px;width:405px;height:94px;border:2px solid var(--orange);border-radius:48px;display:flex;align-items:center;padding-left:48px;gap:24px}
.call-box small{display:block;font-size:14px;color:var(--ink)}
.call-box b{font-size:29px;font-weight:500;color:var(--orange-deep)}
.review{left:0;top:2130px;width:1200px;text-align:center}
.review-badge{display:inline-block;width:130px;height:44px;border-radius:6px;background:#f2f2f2}
.review p{font-size:16px;color:var(--ink);margin-top:2px}

/* estimate */
.ways-title{left:396px;top:2357px;font-size:38px;line-height:44px;color:#fff}
.way{display:flex;align-items:center;gap:22px}
.way .hex{width:92px;height:92px;flex:none}
.way h4{font-family:"Saira Condensed",sans-serif;font-weight:700;font-variant:small-caps;font-size:21px;color:#fff}
.way p{font-size:11px;line-height:19px;color:#fff;width:290px}

/* pricing */
.price-title{left:0;top:2965px;width:1200px;text-align:center;font-size:38px}
.price-copy{left:320px;top:3028px;width:560px;text-align:center;font-size:12px;line-height:21px;color:var(--text)}
.tier{width:230px;text-align:center;top:3120px}
.tier p{font-size:14px;line-height:20px;color:var(--text);margin-top:18px}
.price-btns{left:478px;top:3437px;display:flex;gap:10px}
.price-btns .btn{width:126px;height:42px;line-height:42px}

/* area */
.area-title{left:0;top:3633px;width:1200px;text-align:center;font-size:38px}
.area-copy{left:0;top:3695px;width:1200px;text-align:center;font-size:12.5px;color:var(--muted)}
.locate{left:403px;top:3727px;width:410px;height:40px;border-radius:22px;background:#f1f1f1;display:flex;align-items:center;padding-left:18px;font-size:12px;color:var(--muted)}
.locate .btn{position:absolute;right:0;top:0;width:98px;height:40px;line-height:40px;font-size:16px}
.towns{display:grid;grid-template-columns:150px 150px;row-gap:8px;left:488px;top:3790px;list-style:none}
.towns li{font-size:12.5px;line-height:19px;display:flex;align-items:center;gap:14px}
.towns li::before{content:"";width:6px;height:6px;border:2px solid var(--orange-deep);transform:rotate(45deg)}

/* newsletter */
.newsletter{top:3995px;left:0;width:1200px;height:136px;background:var(--band)}
.news-title{left:200px;top:4040px;font-size:22px;color:#fff}
.news-copy{left:200px;top:4074px;font-size:12px;color:#fff}
.news-form{left:628px;top:4045px;width:465px;height:40px;border-radius:22px;background:#fff;font-size:12px;color:var(--muted);display:flex;align-items:center;padding-left:18px}
.news-form .btn{position:absolute;right:0;top:0;width:120px;height:40px;line-height:40px;font-size:17px}

/* footer */
.footer-mark{left:115px;top:4215px;width:146px;height:146px;border-radius:50%;background:var(--ink);display:flex;align-items:center;justify-content:center;text-align:center;font-family:"Saira Condensed",sans-serif;font-weight:700;font-size:22px;line-height:22px;color:#fff;padding:12px}
.fb-dot{left:181px;top:4382px;width:14px;height:14px;border-radius:50%;background:var(--orange-deep)}
.fcol h5{font-family:"Saira Condensed",sans-serif;font-weight:700;font-variant:small-caps;font-size:17px;color:var(--ink);margin-bottom:14px}
.fcol ul{list-style:none}
.fcol li{font-size:11.5px;line-height:26px;color:var(--muted);display:flex;align-items:center;gap:12px}
.fcol.bul li::before{content:"";width:5px;height:5px;border-radius:50%;background:var(--orange-deep)}
.contact-row{display:flex;gap:14px;font-size:11.5px;line-height:20px;color:var(--muted);margin-bottom:18px}
.contact-row svg{flex:none}
.copyright{left:0;top:4432px;width:1200px;text-align:center;font-size:11px;color:var(--text)}
</style>
</head>
<body>

<!-- Header -->
<header class="abs site-header">
  <div class="abs brand"><span class="brand-dot"></span><span class="brand-name">BRIGHTMOOR JUNK CARTERS</span></div>
  <nav class="abs nav">
    <span class="active">HOME</span><span>OUR SERVICES</span><span>WHAT WE TAKE</span><span>SERVICES AREAS</span><span>CONTACT US</span>
  </nav>
  <div class="abs nav-phone"><i><svg width="16" height="16" viewBox="0 0 24 24"><path fill="#f7901e" d="M6.6 10.8a15.1 15.1 0 0 0 6.6 6.6l2.2-2.2c.3-.3.7-.4 1-.2 1.1.4 2.3.6 3.6.6.6 0 1 .4 1 1V20c0 .6-.4 1-1 1A17 17 0 0 1 3 4c0-.6.4-1 1-1h3.5c.6 0 1 .4 1 1 0 1.3.2 2.5.6 3.6.1.3 0 .7-.2 1z"/></svg></i>+1 (208) 555-0147</div>
</header>

<!-- Hero -->
<svg class="abs" style="left:0;top:70px" width="1200" height="658" viewBox="0 0 1200 658">
  <defs>
    <linearGradient id="heroPhoto" x1="0" y1="0" x2="1" y2="1"><stop offset="0" stop-color="#6e7b5a"/><stop offset=".5" stop-color="#4d4a44"/><stop offset="1" stop-color="#8a8f8f"/></linearGradient>
    <linearGradient id="heroOrange" x1="0" y1="0" x2="1" y2="1"><stop offset="0" stop-color="#f7901e"/><stop offset="1" stop-color="#ef6a12"/></linearGradient>
  </defs>
  <polygon points="30,30 300,0 330,100 280,260 0,240" fill="#fdf3e2"/>
  <g role="img" aria-label="Photo collage of the crew loading junk, trucks and cleared yards">
    <polygon points="580,0 1200,0 1200,658 455,658" fill="url(#heroPhoto)"/>
    <polygon points="455,658 640,470 820,658" fill="url(#heroOrange)" opacity=".9"/>
    <polygon points="640,0 760,0 700,60" fill="url(#heroOrange)" opacity=".85"/>
    <polygon points="1030,0 1200,0 1200,170" fill="url(#heroOrange)" opacity=".8"/>
    <polygon points="960,658 1200,420 1200,658" fill="#c96b1f" opacity=".6"/>
    <g stroke="#fff" stroke-width="5" fill="none">
      <line x1="455" y1="658" x2="1110" y2="0"/><line x1="640" y1="0" x2="1200" y2="560"/>
      <line x1="580" y1="0" x2="1200" y2="630"/><line x1="820" y1="658" x2="1200" y2="280"/>
      <line x1="700" y1="300" x2="1000" y2="0"/>
    </g>
  </g>
</svg>
<div class="abs hero-tag">Fast, Friendly &amp; Professional....</div>
<h1 class="abs display hero-title">Best Rated Junk Removal &amp; Property Cleanout Company in the Treasure Valley</h1>
<div class="abs hero-btns"><span class="btn">Book Now</span><span class="btn">Get Estimate</span></div>
<div class="abs scroll">Scroll Down</div>
<div class="abs scroll-line"></div>

<div class="abs band"><p>Professional Junk Removal ,Same &amp; Next Day Service Available!</p><span class="btn">Book Now</span></div>

<!-- About -->
<div class="abs about-bg"></div>
<svg class="abs" style="left:0;top:805px" width="460" height="410" viewBox="0 0 460 410" role="img" aria-label="Photo of the owner standing beside the branded box truck">
  <defs><linearGradient id="truck" x1="0" y1="0" x2="1" y2="1"><stop offset="0" stop-color="#7fa7cf"/><stop offset=".55" stop-color="#dcdcdc"/><stop offset="1" stop-color="#6c7a52"/></linearGradient></defs>
  <path d="M0 0H430Q456 0 456 26V250L210 410L0 300Z" fill="url(#truck)"/>
</svg>
<div class="abs about-eyebrow">Brightmoor Junk Carters</div>
<h2 class="abs display about-title">Junk Removal and <span class="accent">Hauling</span></h2>
<p class="abs about-copy">The Best Rated Junk Hauling and Cleanout Service in the Boise Metro area. Fastest Response time with Same Day &amp; Next Day service available. We're the Friendliest and Most Professional junk haulers serving Boise, Meridian, Eagle, Star, Middleton, Caldwell, Nampa, Kuna and all of the Treasure Valley.</p>
<div class="abs about-call">Call us Today ! 208-555-0147</div>

<!-- Services -->
<div class="abs eyebrow" style="top:1237px">What We Do</div>
<h2 class="abs display section-title" style="top:1255px">Our <span class="accent">Services</span></h2>

<article class="abs card" style="left:104px">
  <div class="photo" role="img" aria-label="Photo of a pile of household junk on a lawn" style="background:linear-gradient(180deg,#7b9a5a,#3e4a5a)"></div>
  <h3 class="display">Junk Removal</h3>
  <ul><li>Misc. Household Junk</li><li>Furniture Removal</li><li>Mattress Removal</li><li>Appliance Removal</li><li>Hot Tub Removal</li><li>Yard Debris Removal</li><li>Remodeling Debris</li><li>Construction Debris</li><li>Play Structure Removal</li><li>Shed Removal</li></ul>
</article>
<article class="abs card" style="left:448px">
  <div class="photo" role="img" aria-label="Photo of a cleared backyard patio" style="background:linear-gradient(180deg,#c9cfd2,#c7b98a 60%,#8a7d5a)"></div>
  <h3 class="display">Property Cleanouts</h3>
  <ul><li>Estate Cleanouts</li><li>Residential Cleanouts</li><li>Garage Cleanouts</li><li>Storage Unit Cleanouts</li><li>Foreclosure Cleanouts</li><li>Hoarder Cleanouts</li><li>Attic/Basement Cleanouts</li><li>Business/Office Cleanouts</li><li>Mobile Home Cleanout</li><li>House Cleanout</li></ul>
</article>
<article class="abs card" style="left:792px">
  <div class="photo" role="img" aria-label="Photo of the truck parked at a demolition site" style="background:linear-gradient(180deg,#b9bec2,#8e9478 60%,#6a6a5a)"></div>
  <h3 class="display">Light Demolition &amp; Tear Down</h3>
  <ul><li>Shed Removal</li><li>Fence Removal</li><li>Deck Removal</li><li>HotTub Removal</li><li>Play Structure Removal</li><li>Swingset Removal</li><li>Gazebo Removal</li><li>Above-Ground Removal</li><li>Misc. Small Structure</li><li></li></ul>
</article>

<p class="abs display pitch">Your Professional &amp; Friendly Junk Removal Experts You Call ,We Haul ! We'll<br>solve All Your Junk Removal &amp; Property Cleanout Problems!</p>
<div class="abs call-box">
  <svg width="60" height="50" viewBox="0 0 60 50"><path fill="#f7901e" d="M8 6c3-2 6 0 8 4l3 6c1 2 0 4-2 5l-3 2c2 6 6 11 12 14l2-3c1-2 3-3 5-2l6 3c4 2 5 5 3 8-3 5-8 6-14 3C16 40 6 28 3 16 2 11 4 8 8 6z"/><rect x="24" y="4" width="32" height="22" rx="2" fill="none" stroke="#111" stroke-width="2"/><path d="M24 6l16 11 16-11" fill="none" stroke="#111" stroke-width="2"/></svg>
  <div><small>Call or Text us today at</small><b>(208) 555-0147</b></div>
</div>
<div class="abs review"><span class="review-badge"></span><p>Read our reviews</p></div>

<!-- Estimate -->
<svg class="abs" style="left:0;top:2288px" width="1200" height="612" viewBox="0 0 1200 612">
  <defs>
    <linearGradient id="est" x1="0" y1="0" x2="0" y2="1"><stop offset="0" stop-color="#ef6a12"/><stop offset="1" stop-color="#fba01e"/></linearGradient>
    <linearGradient id="estTruck" x1="0" y1="0" x2="1" y2="0"><stop offset="0" stop-color="#e9e9e9"/><stop offset=".3" stop-color="#3a3a3a"/><stop offset="1" stop-color="#1e1e1e"/></linearGradient>
  </defs>
  <polygon points="420,0 1090,0 840,612 135,612" fill="url(#est)"/>
  <rect x="720" y="250" width="420" height="250" rx="14" fill="url(#estTruck)" role="img" aria-label="Photo of the branded box truck with the owner"/>
</svg>
<h2 class="abs display ways-title">3 Simple Ways To<br>Get Your Estimate Today !</h2>
<div class="abs way" style="left:328px;top:2482px">
  <svg class="hex" viewBox="0 0 92 92"><polygon points="46,2 86,25 86,67 46,90 6,67 6,25" fill="#fff"/><path fill="#f7901e" d="M30 32c2-1 4 0 5 2l2 5c1 1 0 3-1 4l-2 1c2 5 5 8 9 10l1-2c1-1 3-2 4-1l5 2c2 1 3 3 2 5-2 4-6 5-10 3-8-3-15-10-18-19-1-4 1-8 3-10z"/></svg>
  <div><h4>Click to Call</h4><p>CALL US today and talk to one of our friendly, local staff members.</p></div>
</div>
<div class="abs way" style="left:285px;top:2600px">
  <svg class="hex" viewBox="0 0 92 92"><polygon points="46,2 86,25 86,67 46,90 6,67 6,25" fill="#fff"/><rect x="26" y="30" width="36" height="24" rx="4" fill="#f7901e"/><path d="M32 54l0 8 8-8z" fill="#f7901e"/><circle cx="36" cy="42" r="2" fill="#fff"/><circle cx="44" cy="42" r="2" fill="#fff"/><circle cx="52" cy="42" r="2" fill="#fff"/></svg>
  <div><h4>Click to Text</h4><p>TEXT US today with photos of the stuff you would like removed.</p></div>
</div>
<div class="abs way" style="left:242px;top:2718px">
  <svg class="hex" viewBox="0 0 92 92"><polygon points="46,2 86,25 86,67 46,90 6,67 6,25" fill="#fff"/><rect x="26" y="34" width="40" height="26" rx="2" fill="#f7901e"/><path d="M26 34l20 14 20-14" fill="none" stroke="#fff" stroke-width="2"/></svg>
  <div><h4>Click to Email</h4><p>EMAIL US today what you would like us to haul Away.</p></div>
</div>

<!-- Pricing -->
<div class="abs" style="left:0;top:2900px;width:1200px;height:665px;background:linear-gradient(180deg,#f6f6f6,#ececec)" role="img" aria-label="Faded background photo of the company truck"></div>
<h2 class="abs display price-title">Bigger Truck, <span class="accent">Better Pricing !</span></h2>
<p class="abs price-copy">Brightmoor Junk Carters is a local family owned and operated business and not a large national franchise. That means we don't have to pass along the 10-15% franchise fee on to our customers like our competitors.</p>
<div class="abs tier" style="left:215px">
  <svg width="200" height="222" viewBox="0 0 200 222"><polygon points="100,4 194,58 194,164 100,218 6,164 6,58" fill="#fff" stroke="#f7b51e" stroke-width="8"/><rect x="35" y="80" width="130" height="62" rx="4" fill="#2b2b2b" role="img" aria-label="Illustration of our box truck"/></svg>
  <p>7 Pickup loads 560 cubic<br>feet 21 cubic yards</p>
</div>
<div class="abs tier" style="left:500px">
  <svg width="200" height="222" viewBox="0 0 200 222"><polygon points="100,4 194,58 194,164 100,218 6,164 6,58" fill="#fff" stroke="#f7901e" stroke-width="8"/><rect x="35" y="82" width="130" height="58" rx="4" fill="#d72f22" role="img" aria-label="Illustration of a competitor's red truck"/></svg>
  <p>6 Pickup loads 480 cubic<br>feet 18 cubic yards</p>
</div>
<div class="abs tier" style="left:785px">
  <svg width="200" height="222" viewBox="0 0 200 222"><polygon points="100,4 194,58 194,164 100,218 6,164 6,58" fill="#fff" stroke="#f3c6c6" stroke-width="2"/><rect x="45" y="86" width="110" height="48" rx="4" fill="#253a8a" role="img" aria-label="Illustration of a competitor's blue truck"/></svg>
  <p>5 Pickup loads 400 cubic<br>feet 15 cubic yards</p>
</div>
<div class="abs price-btns"><span class="btn">Priceing</span><span class="btn">Get Estimate</span></div>

<!-- Service area -->
<svg class="abs" style="left:905px;top:3565px" width="295" height="318" viewBox="0 0 295 318" role="img" aria-label="Photo of the truck loaded at a job site"><defs><linearGradient id="site" x1="0" y1="0" x2="0" y2="1"><stop offset="0" stop-color="#b7bfc5"/><stop offset=".6" stop-color="#56594e"/><stop offset="1" stop-color="#7a7c5c"/></linearGradient></defs><path d="M0 0H295V318L160 270L0 160Z" fill="url(#site)"/></svg>
<svg class="abs" style="left:0;top:3760px" width="265" height="235" viewBox="0 0 265 235" role="img" aria-label="Photo of a town welcome sign"><defs><linearGradient id="sign" x1="0" y1="0" x2="0" y2="1"><stop offset="0" stop-color="#9fc0e0"/><stop offset=".6" stop-color="#5f7c44"/><stop offset="1" stop-color="#4a6a34"/></linearGradient></defs><path d="M0 40L80 0L265 90V235H0Z" fill="url(#sign)"/></svg>
<h2 class="abs display area-title">Services <span class="accent">Area</span></h2>
<p class="abs area-copy">Click on a state or enter your zip code to find a Brightmoor services your area.</p>
<div class="abs locate"><svg width="12" height="16" viewBox="0 0 12 16" style="margin-right:8px"><path d="M6 0a6 6 0 0 1 6 6c0 4-6 10-6 10S0 10 0 6a6 6 0 0 1 6-6z" fill="#777"/><circle cx="6" cy="6" r="2" fill="#f1f1f1"/></svg>Enter Location<span class="btn">Locate !</span></div>
<ul class="abs towns"><li>Boise</li><li>Caldwell</li><li>Meridian</li><li>Middleton</li><li>Eagle</li><li>Garden City</li><li>Star</li><li>Kuna</li><li>Nampa</li><li>Emmett</li></ul>

<!-- Newsletter -->
<div class="abs newsletter"></div>
<svg class="abs" style="left:132px;top:4040px" width="52" height="44" viewBox="0 0 52 44"><rect x="2" y="10" width="40" height="28" rx="2" fill="none" stroke="#f7901e" stroke-width="2.5"/><path d="M2 12l20 14 20-14" fill="none" stroke="#f7901e" stroke-width="2.5"/><circle cx="42" cy="34" r="8" fill="#0c0c0c" stroke="#f7901e" stroke-width="2.5"/></svg>
<h3 class="abs display news-title">Newsletter <span class="accent">Signup !</span></h3>
<p class="abs news-copy">Would you like to receive our exclusive update for Signup !</p>
<div class="abs news-form">Enter Email<span class="btn">Subscribe</span></div>

<!-- Footer -->
<div class="abs footer-mark">BRIGHTMOOR JUNK CARTERS</div>
<span class="abs fb-dot"></span>
<div class="abs fcol bul" style="left:342px;top:4175px"><h5>Sitemap</h5><ul><li>Home</li><li>Our Services</li><li>What We Take</li><li>Services Areas</li><li>Contact Us</li></ul></div>
<div class="abs fcol bul" style="left:624px;top:4175px"><h5>Services</h5><ul><li>Junk Removal</li><li>Property Cleanout</li><li>Light Demolition</li><li>Dumpster Rental</li></ul></div>
<div class="abs fcol" style="left:905px;top:4175px"><h5>Contact Us</h5>
  <div class="contact-row"><svg width="18" height="18" viewBox="0 0 24 24"><path fill="#ef6a12" d="M6.6 10.8a15.1 15.1 0 0 0 6.6 6.6l2.2-2.2c.3-.3.7-.4 1-.2 1.1.4 2.3.6 3.6.6.6 0 1 .4 1 1V20c0 .6-.4 1-1 1A17 17 0 0 1 3 4c0-.6.4-1 1-1h3.5c.6 0 1 .4 1 1 0 1.3.2 2.5.6 3.6.1.3 0 .7-.2 1z"/></svg><span>+1 (208) 555-0147</span></div>
  <div class="contact-row"><svg width="18" height="22" viewBox="0 0 12 16"><path d="M6 0a6 6 0 0 1 6 6c0 4-6 10-6 10S0 10 0 6a6 6 0 0 1 6-6z" fill="#ef6a12"/><circle cx="6" cy="6" r="2" fill="#fff"/></svg><span>Brightmoor Junk Carters<br>1180 W Alder Crest Ln, Meridian , ID<br>83646, Unite Sattes</span></div>
  <div class="contact-row"><svg width="18" height="18" viewBox="0 0 20 20"><circle cx="10" cy="10" r="8.5" fill="none" stroke="#ef6a12" stroke-width="2"/><path d="M10 5v5l3 2" stroke="#ef6a12" stroke-width="2" fill="none"/></svg><span>WORKING HOURS<br>Mon to Sat – 8 AM to 6 PM</span></div>
</div>
<p class="abs copyright">©<span class="accent">Brightmoor Junk Carters</span> - 2021 All rights reserved.</p>

</body>
</html>
```